Business card design needed

We need a business card for a new business. We are called Tiny Toilers Gear, and we make replica kid size clothing, mainly hi vis shirts, work trousers and shorts. Our long term goal is to include clothing for numerous trades and professions, for our littlest Aussies. We would like a kid friendly card using navy blue, bright orange, bright yellow and bright pink. We haven't set up our web page yet because we want to base it on our final business card design.
Updates

Industry/Entity Type

Clothing

```html
<!DOCTYPE html>
<html lang="en">
<head>
<meta charset="utf-8">
<title>Tiny Toilers Gear – Business Card</title>
<link rel="stylesheet" href="https://fonts.googleapis.com/css2?family=Delius&display=swap">
<style>
  :root {
    --navy: #0b1a5c;
    --navy-light: #1c2f7a;
    --orange: #ff9a33;
    --pink: #ff0a8c;
    --yellow: #ffff1a;
    --white: #ffffff;
    --ink: #111111;
    --brown: #6b2a22;
    --brown-light: #8a3c30;
  }
  * { margin: 0; padding: 0; box-sizing: border-box; }
  html, body {
    width: 1200px;
    height: 741px;
    overflow: hidden;
    background: #ffffff;
  }
  .card {
    position: relative;
    width: 1200px;
    height: 741px;
    overflow: hidden;
    background: radial-gradient(circle at 560px 560px, var(--navy-light) 0%, var(--navy) 60%);
    font-family: "Delius", "Comic Sans MS", cursive;
  }
  .card-shapes {
    position: absolute;
    inset: 0;
  }
  .mascot-art {
    position: absolute;
    left: 45px;
    top: 140px;
    width: 335px;
    height: 440px;
    border-radius: 48% 48% 46% 46%;
    background: radial-gradient(circle at 50% 60%, var(--brown-light) 0%, var(--brown) 75%);
  }
  .mascot-shadow {
    position: absolute;
    left: 120px;
    top: 612px;
    width: 200px;
    height: 26px;
    border-radius: 50%;
    background: radial-gradient(ellipse at center, rgba(90, 0, 40, 0.45) 0%, rgba(90, 0, 40, 0) 70%);
  }
  .holder {
    position: absolute;
    right: 45px;
    top: 14px;
    text-align: right;
  }
  .holder-name {
    color: var(--white);
    font-size: 55px;
    line-height: 1.1;
  }
  .holder-title {
    color: var(--ink);
    font-size: 31px;
    line-height: 1.1;
  }
  .brand-name {
    position: absolute;
    left: 392px;
    top: 205px;
    width: 770px;
    text-align: center;
    color: var(--yellow);
    font-size: 82px;
    line-height: 1;
    white-space: nowrap;
  }
  .contact-list {
    position: absolute;
    left: 565px;
    top: 385px;
    list-style: none;
    color: var(--white);
    font-size: 44px;
    line-height: 84px;
  }
  .contact-item {
    display: flex;
    align-items: flex-start;
    white-space: nowrap;
  }
  .contact-icon {
    flex: 0 0 48px;
    height: 84px;
    display: flex;
    align-items: center;
  }
  .contact-icon svg { display: block; }
  .contact-item--address .contact-text { line-height: 84px; }
</style>
</head>
<body>
  <main class="card">
    <svg class="card-shapes" width="1200" height="741" viewBox="0 0 1200 741" aria-hidden="true">
      <polygon class="top-band" points="0,0 1200,0 1200,189 427,103 0,60" fill="var(--orange)"/>
      <circle class="side-disc" cx="-49" cy="411" r="548" fill="var(--pink)"/>
    </svg>

    <div class="mascot-shadow" aria-hidden="true"></div>
    <div class="mascot-art" role="img" aria-label="Cheerful cartoon kid mascot with a brown tuft of hair"></div>

    <header class="holder">
      <p class="holder-name">Your Name</p>
      <p class="holder-title">Job Title</p>
    </header>

    <h1 class="brand-name">Tiny Toilers Gear</h1>

    <ul class="contact-list">
      <li class="contact-item contact-item--address">
        <span class="contact-icon">
          <svg width="20" height="28" viewBox="0 0 20 28" aria-hidden="true">
            <path d="M10 1C5 1 1.5 4.8 1.5 9.5 1.5 16 10 27 10 27s8.5-11 8.5-17.5C18.5 4.8 15 1 10 1z" fill="var(--white)"/>
            <circle cx="10" cy="9.5" r="3.4" fill="var(--navy)"/>
          </svg>
        </span>
        <span class="contact-text">Your House, Your Street,<br>Town, Country-Postcode</span>
      </li>
      <li class="contact-item contact-item--phone">
        <span class="contact-icon">
          <svg width="22" height="30" viewBox="0 0 22 30" aria-hidden="true">
            <rect x="2" y="1" width="18" height="28" rx="3" fill="var(--white)"/>
            <rect x="5" y="4" width="12" height="8" fill="var(--navy)"/>
            <g fill="var(--navy)">
              <rect x="5" y="15" width="3" height="3"/><rect x="9.5" y="15" width="3" height="3"/><rect x="14" y="15" width="3" height="3"/>
              <rect x="5" y="20" width="3" height="3"/><rect x="9.5" y="20" width="3" height="3"/><rect x="14" y="20" width="3" height="3"/>
            </g>
          </svg>
        </span>
        <span class="contact-text">0123 564789</span>
      </li>
      <li class="contact-item contact-item--email">
        <span class="contact-icon">
          <svg width="30" height="22" viewBox="0 0 30 22" aria-hidden="true">
            <rect x="1.5" y="1.5" width="27" height="19" fill="none" stroke="var(--white)" stroke-width="2"/>
            <polyline points="1.5,1.5 15,12 28.5,1.5" fill="none" stroke="var(--white)" stroke-width="2"/>
          </svg>
        </span>
        <span class="contact-text">you@yourmail.com</span>
      </li>
    </ul>
  </main>
</body>
</html>
```